Commit to H.E.A.L. (Healthy Eating and Living)Corporate Wellness

Rise with B.R.I.G.H.T. (Balanced Habits In Good Routines Today) is my health and wellness company. I am a certified Health & Lifestyle Coach who provides a 6 month one-on-one coaching program for individuals and groups. I also provide 1 hour health seminars or "brown bag" lunches for any type of organization. My focus is on prevention of chronic disease through health and food education, as well as effective lifestyle coaching. I would like the brochure to have my logo, my name and certification, some health statistics, and my programs/seminars. Looking for a one page, half fold or trifold brochure design. I am flexible! I forgot to include my personal information. phone number 555/314-0872. email is marla@teachandthrivenation.example. website is www.risewithbright.example.

Target Market(s)

Companies (large or small) looking for wellness and disease prevention programs for their employees.

Industry/Entity Type

Health

Requirements
Must have
• I am going into this with no picture in my head as to what I want. I like simplicity. I like to represent health, in all aspects, from food to environment. I will attach my logo to use, and colors should accent the logo.
I need it to include my name and title (Marla Vesterling, Certified Health & Lifestyle Coach). The tag line "Because your workforce's wellbeing IS your bottom line." These statistics listed clearly: "1. The U.S. spends $2.8 trillion on health care every year, and this number is rising. 2. Treating individuals with chronic preventable disease is responsible for 75% of our health care costs. 3. The U.S. spends more on healthcare than Japan, Germany, France, China, UK, Italy, Canada, Brazil, Spain and Australia COMBINED. 4. The Global Vitality Council ranks the U.S. 37th for overall health outcomes. This means that more healthcare spending does not equate to better health.
Then it needs to say that "Our healthcare costs are out of control, increasing, and unsustainable. We do not have a healthcare system, we have a disease care system. Prevention of chronic disease is the only way to reduce our costs. Workplace wellness solutions MUST change behaviors. Food and health education, as well as effective lifestyle coaching are the keys to this behavior change."
I offer 1 hour seminars, sample seminars include but are not limited to "Tumor Avoidance" "Nation's Plate/Nation's Ailment," and "Vitality & Balance starts when Old Routines Stop." I also offer a six month bi-weekly health coaching program for individuals or small groups. Plus custom programs that include health food store tours, pantry purges, cooking ideas and preparation, etc.

```html
<!DOCTYPE html>
<html lang="en">
<head>
<meta charset="utf-8">
<title>Brightwell Wellness — Corporate Wellness</title>
<link href="https://fonts.googleapis.com/css2?family=Arimo:wght@400;700&family=Quicksand:wght@500&family=Tinos:wght@400;700&display=swap" rel="stylesheet">
<style>
  :root {
    --green-deep: #3b6a27;
    --green-mid: #5a8c35;
    --green-soft: #8fb658;
    --lime: #b3d22f;
    --paper: #efefeb;
    --olive-dark: #3e3a28;
    --ink: #3a3a34;
    --white: #ffffff;
  }
  * { margin: 0; padding: 0; box-sizing: border-box; }
  html, body { width: 936px; height: 1200px; overflow: hidden; background: var(--white); }
  .flyer {
    position: absolute; left: 19px; top: 18px; width: 898px; height: 1164px;
    overflow: hidden; background: var(--green-mid);
  }
  .hero-photo {
    position: absolute; inset: 0;
    background:
      radial-gradient(ellipse 260px 190px at 600px 300px, rgba(196,214,120,.55), transparent 70%),
      radial-gradient(ellipse 300px 200px at 230px 60px, rgba(214,230,150,.6), transparent 70%),
      radial-gradient(ellipse 180px 130px at 520px 300px, rgba(140,110,60,.55), transparent 70%),
      linear-gradient(180deg, #6d9440 0%, var(--green-mid) 40%, var(--green-deep) 75%, #4d7d2f 100%);
  }
  .curve { position: absolute; inset: 0; }
  .tagline {
    position: absolute; right: 47px; top: 176px; text-align: right;
    font-family: "Quicksand", sans-serif; font-weight: 500; color: var(--white); line-height: 1.05;
  }
  .tagline .small { font-size: 30px; }
  .tagline .big { font-size: 46px; }
  .manifesto {
    position: absolute; left: 55px; top: 362px; width: 780px;
    font-family: "Tinos", serif; font-size: 22px; line-height: 25.5px; color: var(--white);
  }
  .stats {
    position: absolute; left: 55px; top: 546px; width: 460px; list-style: none;
    font-family: "Tinos", serif; font-size: 15.5px; line-height: 17px; color: var(--white);
  }
  .stats li { margin-bottom: 17px; }
  .coach-photo {
    position: absolute; left: 59px; top: 789px; width: 205px; height: 190px;
    border: 4px solid var(--green-soft);
    background: linear-gradient(160deg, #3f5a2c, #6f8b4e 55%, #d9c6a8);
  }
  .coach-name {
    position: absolute; left: 55px; top: 999px;
    font-family: "Arimo", sans-serif; color: var(--white);
  }
  .coach-name .name { font-size: 18px; }
  .coach-name .title { font-size: 13px; margin-top: 3px; }
  .brand {
    position: absolute; left: 400px; top: 912px; width: 440px;
    display: flex; align-items: center; justify-content: center; gap: 12px;
    font-family: "Quicksand", sans-serif; font-weight: 500; font-size: 34px; color: var(--green-mid);
  }
  .brand-dot { width: 22px; height: 22px; border-radius: 50%; background: var(--lime); }
  .contact {
    position: absolute; left: 400px; top: 974px; width: 440px; text-align: center;
    font-family: "Arimo", sans-serif; font-style: normal; color: var(--ink);
  }
  .contact .phone { font-size: 24px; font-weight: 700; line-height: 30px; }
  .contact .line { font-size: 19px; line-height: 24px; }
  .seminars {
    position: absolute; left: 0; top: 1070px; width: 898px; height: 94px;
    background: var(--olive-dark); color: var(--white); text-align: center;
    font-family: "Arimo", sans-serif; padding-top: 12px;
  }
  .seminars h2 { font-size: 17px; font-weight: 700; line-height: 22px; }
  .seminars p { font-size: 19px; line-height: 24px; }
</style>
</head>
<body>
<main class="flyer">
  <div class="hero-photo" role="img" aria-label="Close-up photograph of a halved avocado on a green background"></div>

  <svg class="curve" width="898" height="1164" viewBox="0 0 898 1164" aria-hidden="true">
    <circle cx="922" cy="1335" r="718" fill="var(--lime)"/>
    <circle cx="922" cy="1335" r="692" fill="var(--paper)"/>
  </svg>

  <h1 class="tagline">
    <span class="small">Because </span><span class="big">your workforce's</span><span class="small"> wellbeing</span><br>
    <span class="small">IS </span><span class="big">your bottom line</span>
  </h1>

  <p class="manifesto">“Our healthcare costs are out of control, increasing, and unsustainable.<br>
    We do not have a healthcare system, we have a disease care system.<br>
    Prevention of chronic disease is the only way to reduce our costs.<br>
    Workplace wellness solutions MUST change behaviors.<br>
    Food and health education, as well as effective lifestyle coaching are<br>
    the keys to this behavior change."</p>

  <ul class="stats">
    <li>The U.S. spends <b>$2.8 trillion</b> on health care every year,<br>and this number is rising.</li>
    <li>Treating individuals with chronic preventable disease<br>is responsible for <b>75%</b> of our health care costs.</li>
    <li>The U.S. spends more on <b>healthcare</b> than Japan,<br>Germany, France, China, UK, Italy, Canada, Brazil,<br>Spain and Australia COMBINED.</li>
    <li>The Global Vitality Council ranks<br>the U.S. <b>37th</b> for overall health outcomes.</li>
  </ul>

  <div class="coach-photo" role="img" aria-label="Portrait photograph of the coach outdoors"></div>
  <div class="coach-name">
    <p class="name">Marla Vesterling</p>
    <p class="title">Certified Health &amp; Lifestyle Coach</p>
  </div>

  <div class="brand"><span class="brand-dot"></span><span>Brightwell Wellness</span></div>

  <address class="contact">
    <p class="phone">555/314-0872</p>
    <p class="line">marla@teachandthrivenation.example</p>
    <p class="line">www.risewithbright.example</p>
  </address>

  <section class="seminars">
    <h2>JOIN TO 1 HOUR SEMINARS</h2>
    <p>Tumor Avoidance | Nation's Plate/Nation's Ailment</p>
    <p>Vitality &amp; Balance starts when Old Routines Stop</p>
  </section>
</main>
</body>
</html>
```